Post card for landscape service

Velmora Property Management**FEATURED SERVICE*** Weekly Lawn mowing service starting at $15/ cutting ****other services****landscape servicespring and fall clean uplawn and flowerbed care (pest and weed control)fertilizing plantingand moreCall for a Free estimate!!10% off first months service with signed contract

Please make double sided ( a front and a back)

Target Market(s)

home owners

Industry/Entity Type

Landscape

Requirements
Must have
• please feture the weekly lawn mowing service and then list the other sevices
• contact info... can be found on business card that was uploaded.
• must say residential services
Should not have
• please dont list reo management

```html
<!DOCTYPE html>
<html lang="en">
<head>
<meta charset="utf-8">
<title>Velmora Property Management – Postcard</title>
<link rel="stylesheet" href="https://fonts.googleapis.com/css2?family=Oswald:wght@400;500;600;700&family=Montserrat:wght@500;600&family=Roboto+Condensed:wght@400;500;700&display=swap">
<style>
  :root{
    --bg:#ecebe8;
    --paper:#ffffff;
    --green:#1f8a3c;
    --green-dark:#146b2c;
    --green-light:#7fcf77;
    --green-soft:#c8ecc0;
    --cream:#f7f29a;
    --ink:#121212;
    --bar:#0d0f0e;
    --text:#2a2a2a;
    --rule:#c9c9c9;
  }
  *{box-sizing:border-box;margin:0;padding:0}
  html,body{width:1200px;height:1000px;overflow:hidden;background:var(--bg)}
  .canvas{position:relative;width:1200px;height:1000px}

  .card{position:absolute;background:var(--paper);overflow:hidden;box-shadow:0 3px 10px rgba(0,0,0,.25)}

  /* FRONT */
  .front{left:68px;top:25px;width:647px;height:463px}
  .front .photo{position:absolute;left:0;top:0;width:647px;height:260px;
    background:linear-gradient(160deg,#4f8a2b 0%,#3f7f25 35%,#2f6d1e 60%,#b33a22 72%,#262a24 85%,#3c7a28 100%)}
  .front .wave{position:absolute;left:0;top:190px;width:647px;height:90px}
  .brand-front{position:absolute;left:38px;top:30px;font-family:"Oswald",sans-serif;font-weight:700;color:var(--ink);line-height:.95;text-transform:uppercase}
  .brand-front .name{display:block;font-size:72px;letter-spacing:-.5px}
  .brand-front .sub{display:block;font-size:26px;margin-top:2px}
  .feature-tab{position:absolute;left:0;top:238px;width:297px;height:62px;background:var(--green);border-radius:0 10px 0 0;
    font-family:"Oswald",sans-serif;color:#fff;font-size:24px;line-height:1.05;padding:6px 0 0 18px;text-transform:uppercase;font-weight:500;white-space:nowrap}
  .feature-tab .starting{text-transform:none;color:var(--cream);font-size:20px}
  .price-box{position:absolute;left:0;top:306px;width:297px;height:62px;background:var(--green);border-top:2px solid var(--green-light);
    box-shadow:6px 6px 6px rgba(0,0,0,.3)}
  .price-box span{display:block;font-family:"Oswald",sans-serif;font-weight:500;font-size:52px;line-height:62px;color:var(--cream);padding-left:18px;letter-spacing:-.5px;white-space:nowrap}
  .other{position:absolute;left:354px;top:248px;font-family:"Roboto Condensed",sans-serif;color:var(--ink)}
  .other h3{font-family:"Oswald",sans-serif;font-weight:500;color:var(--green);font-size:20px;margin-bottom:4px}
  .other ul{list-style:none}
  .other li{position:relative;font-size:16.5px;line-height:20px;padding-left:16px;margin-bottom:1px;white-space:nowrap}
  .other li svg{position:absolute;left:0;top:5px;width:11px;height:11px}
  .other li.gap{margin-top:4px}
  .cta-bar{position:absolute;left:0;top:395px;width:647px;height:68px;background:var(--bar);display:flex;align-items:center;padding-left:48px}
  .cta-bar .cta{font-family:"Montserrat",sans-serif;font-weight:500;color:var(--green);font-size:17px;line-height:21px;text-transform:uppercase;white-space:nowrap}
  .cta-bar .cta .b{color:var(--green-light)}
  .cta-bar .phone{font-family:"Montserrat",sans-serif;font-weight:600;color:#fff;font-size:38px;margin-left:14px;letter-spacing:-.5px;white-space:nowrap}

  /* BACK */
  .back{left:508px;top:505px;width:649px;height:465px}
  .back .photo{position:absolute;left:0;top:0;width:330px;height:168px;
    background:linear-gradient(180deg,#6d8d5a 0%,#8a4a3a 28%,#3f7a32 55%,#4f9a3a 100%)}
  .back .swoosh{position:absolute;left:0;top:0;width:649px;height:465px}
  .stamp{position:absolute;left:526px;top:20px;width:101px;height:111px;border:1px solid var(--rule)}
  .addr-line{position:absolute;left:377px;width:250px;height:1px;background:var(--rule)}
  .intro{position:absolute;left:22px;top:180px;width:282px;font-family:"Roboto Condensed",sans-serif;font-weight:700;font-size:10.5px;line-height:16px;color:var(--text);text-align:justify}
  .intro .hl{color:var(--green)}
  .offer-band{position:absolute;left:20px;top:254px;width:308px;height:48px;background:var(--green);border-radius:8px 0 0 8px}
  .offer-band p{position:absolute;left:100px;top:4px;font-family:"Roboto Condensed",sans-serif;font-weight:500;color:#fff;font-size:17px;line-height:21px;text-transform:uppercase;white-space:nowrap}
  .badge{position:absolute;left:27px;top:248px;width:75px;height:75px;border-radius:50%;background:var(--green-light);border:3px solid var(--green-soft);
    display:flex;flex-direction:column;align-items:center;justify-content:center;font-family:"Oswald",sans-serif;font-weight:600;color:#fff;font-size:22px;line-height:23px}
  .contact{position:absolute;left:30px;top:320px;width:290px;text-align:center}
  .brand-back{font-family:"Oswald",sans-serif;font-weight:700;color:var(--ink);text-transform:uppercase;line-height:.95}
  .brand-back .name{display:block;font-size:46px}
  .brand-back .sub{display:block;font-size:16px;margin-top:1px}
  .contact .phone{font-family:"Montserrat",sans-serif;font-weight:500;color:var(--green);font-size:18px;margin-top:4px;display:flex;align-items:center;justify-content:center;gap:4px}
  .contact .phone svg{width:15px;height:15px}
  .contact .line{font-family:"Montserrat",sans-serif;font-size:12px;color:var(--text);line-height:18px;white-space:nowrap}
</style>
</head>
<body>
<main class="canvas">

  <section class="card front" aria-label="Postcard front">
    <div class="photo" role="img" aria-label="Photo of a red riding lawn mower cutting a green lawn"></div>
    <svg class="wave" viewBox="0 0 647 90" preserveAspectRatio="none" aria-hidden="true">
      <path d="M0 45 C160 10 330 20 647 10 L647 90 L0 90 Z" fill="var(--green-light)"/>
      <path d="M0 62 C180 30 360 45 647 28 L647 90 L0 90 Z" fill="var(--paper)"/>
    </svg>
    <h1 class="brand-front"><span class="name">Velmora</span><span class="sub">Property Management</span></h1>

    <div class="feature-tab">Weekly Lawn<br>Mowing Service <span class="starting">starting at</span></div>
    <div class="price-box"><span>$15/CUTTING</span></div>

    <div class="other">
      <h3>Other Services</h3>
      <ul>
        <li><svg viewBox="0 0 11 11"><rect x=".5" y=".5" width="10" height="10" fill="none" stroke="#1f8a3c"/><path d="M2 5.5l2.5 2.5L9.5 2" fill="none" stroke="#1f8a3c" stroke-width="1.6"/></svg>Landscape Service</li>
        <li><svg viewBox="0 0 11 11"><rect x=".5" y=".5" width="10" height="10" fill="none" stroke="#1f8a3c"/><path d="M2 5.5l2.5 2.5L9.5 2" fill="none" stroke="#1f8a3c" stroke-width="1.6"/></svg>Spring &amp; Fall Cleanups</li>
        <li><svg viewBox="0 0 11 11"><rect x=".5" y=".5" width="10" height="10" fill="none" stroke="#1f8a3c"/><path d="M2 5.5l2.5 2.5L9.5 2" fill="none" stroke="#1f8a3c" stroke-width="1.6"/></svg>Lawn And Flowerbed Care<br>(Pest And Weed Control)</li>
        <li class="gap"><svg viewBox="0 0 11 11"><rect x=".5" y=".5" width="10" height="10" fill="none" stroke="#1f8a3c"/><path d="M2 5.5l2.5 2.5L9.5 2" fill="none" stroke="#1f8a3c" stroke-width="1.6"/></svg>Fertilizing Planting and More</li>
      </ul>
    </div>

    <div class="cta-bar">
      <p class="cta">Commercial &amp; Residential<br><span class="b">Call for a free estimate!!</span></p>
      <p class="phone">908-555-0142</p>
    </div>
  </section>

  <section class="card back" aria-label="Postcard back">
    <div class="photo" role="img" aria-label="Photo of a brick house with trimmed hedges and a green front lawn"></div>
    <svg class="swoosh" viewBox="0 0 649 465" aria-hidden="true">
      <path d="M360 0 C450 60 400 150 330 230 C300 280 320 380 345 465 L330 465 C300 380 285 280 318 225 C380 150 420 60 340 0 Z" fill="var(--green)"/>
    </svg>
    <div class="stamp"></div>
    <div class="addr-line" style="top:232px"></div>
    <div class="addr-line" style="top:305px"></div>

    <p class="intro"><span class="hl">Velmora Property Management</span> will help you manage yourr properties with services ranging from landscaping, pest control, snow removal and more.</p>

    <div class="offer-band"><p>First months service<br>with signed contract</p></div>
    <div class="badge"><span>10%</span><span>OFF</span></div>

    <div class="contact">
      <h2 class="brand-back"><span class="name">Velmora</span><span class="sub">Property Management</span></h2>
      <p class="phone"><svg viewBox="0 0 16 16" aria-hidden="true"><circle cx="8" cy="8" r="8" fill="#121212"/><path d="M5.2 4.2l1.4-.3.8 1.9-.9.7c.5 1 1.2 1.7 2.2 2.2l.7-.9 1.9.8-.3 1.4c-3 .2-5.9-2.7-5.8-5.8z" fill="#fff"/></svg>908-555-0142</p>
      <p class="line">PO Box 240 Alderbrook, NJ 08810</p>
      <p class="line">velmoraproperty@mailbox.com</p>
    </div>
  </section>

</main>
</body>
</html>
```